Innovative Consulting Firm Needs New Business Cards and Stationary

Our Innovative Consulting Firm, Larkfield Consulting, is in need of new business cards and stationary designs. We want two-sided cards that incorporate our logo, which is attached. We are looking for something not too formal, but is professional and slick.

Card should have the following information:
Name (ex. Tom Bradley)
Title (ex. Manager)
Address (ex. 24680 Cedar Lane)
Address 2 (ex. Suite 100)
City
State
Zip Code
Mobile
Email

The card should also have our website: www.larkfieldconsulting.example

Industry/Entity Type

Management Consulting

Contact Information for Business Card

Name (ex. Tom Bradley)
Title (ex. Manager)
Address 2 (ex. Suite 100)
City
State
Zip Code
Mobile
Email

Font styles to use
Sans Serif

Requirements
Must have
• The colors on the card must match the colors in the logo. The exact color codes are attached in a pdf.
Nice to have
• The Company's Tagline is "Focused on your Future". This might be nice to incorporate, but not necessary.

```html
<!DOCTYPE html>
<html lang="en">
<head>
<meta charset="utf-8">
<title>Larkfield Consulting – Business Card</title>
<link href="https://fonts.googleapis.com/css2?family=Exo+2:wght@400;500&family=Courgette&display=swap" rel="stylesheet">
<style>
  :root {
    --brand-blue: #1b4f9f;
    --brand-orange: #f3a40f;
    --card-orange: #f4a60f;
    --rule-blue: #7ec3dc;
    --paper: #ffffff;
    --backdrop: #ffffff;
  }
  * { margin: 0; padding: 0; box-sizing: border-box; }
  html, body {
    width: 1200px; height: 1001px; overflow: hidden;
    background: var(--backdrop);
    font-family: "Exo 2", sans-serif;
  }
  .canvas { position: relative; width: 1200px; height: 1001px; }
  .card {
    position: absolute; top: 62px; width: 532px; height: 877px;
    box-shadow: 4px 5px 9px rgba(0,0,0,0.35);
  }
  .card--front { left: 39px; background: var(--paper); border: 1px solid #e4e4e4; }
  .card--back { left: 639px; background: var(--card-orange); }

  .holder-name {
    position: absolute; top: 210px; width: 100%; text-align: center;
    font-size: 50px; font-weight: 400; color: var(--brand-blue); letter-spacing: 0.5px;
  }
  .holder-title {
    position: absolute; top: 292px; width: 100%; text-align: center;
    font-size: 26px; color: var(--brand-orange);
  }
  .divider {
    position: absolute; top: 438px; left: 74px; width: 382px; height: 1.5px;
    background: var(--rule-blue);
  }
  .contact-list { position: absolute; top: 656px; left: 52px; list-style: none; }
  .contact-list li {
    position: relative; height: 34.3px; padding-left: 86px;
    font-size: 16px; line-height: 34px; color: var(--brand-blue);
  }
  .contact-list svg {
    position: absolute; left: 26px; top: 50%; transform: translate(-50%, -50%);
    fill: none; stroke: var(--brand-blue); stroke-width: 2;
  }
  .contact-list .icon-fill { fill: var(--brand-blue); stroke: none; }

  .logo-plate {
    position: absolute; top: 394px; left: 86px; width: 360px; height: 96px;
    background: var(--paper);
    display: flex; align-items: center; justify-content: center;
  }
  .logo-name {
    font-size: 40px; font-weight: 500; color: var(--brand-blue); letter-spacing: 0.5px;
  }
  .tagline {
    position: absolute; top: 503px; width: 100%; text-align: center;
    font-family: "Courgette", cursive; font-size: 33px; color: var(--brand-blue);
  }
</style>
</head>
<body>
<main class="canvas">
  <section class="card card--front" aria-label="Card front">
    <h1 class="holder-name">Tom Bradley</h1>
    <p class="holder-title">Manager</p>
    <div class="divider"></div>
    <ul class="contact-list">
      <li>
        <svg width="30" height="34" viewBox="0 0 30 34"><path class="icon-fill" d="M15 1C8 1 3 6 3 12.5 3 21 15 33 15 33s12-12 12-20.5C27 6 22 1 15 1zm0 16a4.5 4.5 0 1 1 0-9 4.5 4.5 0 0 1 0 9z"/></svg>
        24680 Cedar Lane
      </li>
      <li>Suite 100</li>
      <li>
        <svg width="20" height="28" viewBox="0 0 20 28"><rect x="2" y="2" width="16" height="24" rx="1.5"/><line x1="7" y1="22" x2="13" y2="22"/></svg>
        +44 555 0192
      </li>
      <li>
        <svg width="34" height="24" viewBox="0 0 34 24"><rect x="1.5" y="1.5" width="31" height="21"/><polyline points="1.5,1.5 17,13 32.5,1.5"/></svg>
        tombradley@larkfield.example
      </li>
      <li>
        <svg width="26" height="26" viewBox="0 0 26 26"><circle cx="13" cy="13" r="11"/><ellipse cx="13" cy="13" rx="5" ry="11"/><line x1="2" y1="13" x2="24" y2="13"/><line x1="13" y1="2" x2="13" y2="24"/></svg>
        www.larkfieldconsulting.example
      </li>
    </ul>
  </section>

  <section class="card card--back" aria-label="Card back">
    <div class="logo-plate">
      <span class="logo-name">Larkfield Consulting</span>
    </div>
    <p class="tagline">Focused on your Future</p>
  </section>
</main>
</body>
</html>
```